Brochure for Community-Based Therapy Company

Will be given out to patients, doctors, case managers. We are redesigning our marketing materials and would like a design for a brochure. We provide therapy to individuals who have been injured in car accidents or on the job. We provide occupational therapy, speech therapy and psychotherapy. We would like the brochure to utilize our corporate ID and color scheme that we are using for our other materials (see attached letterhead and logo).

Stock photos that are used should stay away from images of outpatient or hospital settings, stay away from photos with obvious disabilities (wheelchairs, learning to walk, etc), and nothing that looks like physical therapy, as we don't provide physical therapy only OT, Speech and psychotherapy. Would prefer to not have people wearing masks, as we will use this beyond the pandemic. Also, our staff wears business casual clothing so would prefer photos that the individuals are not wearing scrubs or other medical attire (lab coats, etc).

Target Market(s)

Patients, Physicians/Doctors, Case Managers

Industry/Entity Type

Healthcare

Requirements
Must have
• Prefer a booklet format but doesn't have to be 8.5 inch by 11 inch (can be a little smaller).

```html
<!DOCTYPE html>
<html lang="en">
<head>
<meta charset="utf-8">
<title>Harborline Therapy Group – Brochure</title>
<link href="https://fonts.googleapis.com/css2?family=Jost:wght@400;500;600&family=Roboto:ital,wght@0,400;0,500;1,400;1,500&display=swap" rel="stylesheet">
<style>
  :root{
    --sage:#8aae9f;
    --sage-dark:#6f9483;
    --white:#ffffff;
    --paper:#f7f7f6;
    --grey:#8a8a8a;
    --grey-dark:#555555;
    --shadow:#9c9c9c;
    --stage:#e6e6e6;
    --photo-warm:#e0a44e;
    --photo-cool:#c9d3dc;
    --photo-dark:#5d5047;
  }
  *{box-sizing:border-box;margin:0;padding:0}
  html,body{width:1200px;height:800px;overflow:hidden}
  body{background:var(--stage);font-family:"Roboto",Arial,sans-serif;position:relative}
  .brochure{position:absolute;left:100px;top:38px;width:1000px;height:724px;display:flex;box-shadow:0 10px 30px rgba(0,0,0,.18)}
  .panel{position:relative;width:500px;height:724px;overflow:hidden}

  /* back panel */
  .panel--back{background:var(--sage);color:var(--white)}
  .headline{position:absolute;left:36px;top:30px;font-family:"Jost",sans-serif;font-weight:500;font-size:27px;line-height:1.2;letter-spacing:1.6px;text-transform:uppercase}
  .approach{position:absolute;left:36px;top:106px;width:428px}
  .approach p{font-size:7.4px;line-height:1.38;text-align:justify;margin-bottom:8px}
  .serve-title{position:absolute;left:36px;top:348px;font-family:"Jost",sans-serif;font-weight:500;font-size:45px;line-height:1.15;letter-spacing:2px;text-transform:uppercase}
  .serve-intro{position:absolute;left:282px;top:352px;width:186px;font-size:8.4px;font-style:italic;font-weight:500;line-height:1.4}
  .serve-intro p{margin-bottom:10px}
  .tag{position:absolute;left:36px;background:var(--white);color:var(--sage-dark);font-family:"Jost",sans-serif;font-weight:500;font-size:9px;letter-spacing:1px;text-transform:uppercase;padding:3px 10px;white-space:nowrap}
  .tag--diagnoses{top:474px}
  .tag--funding{top:566px}
  .diagnoses{position:absolute;top:500px;list-style:none;font-size:7.6px;line-height:1.5}
  .diagnoses li::before{content:"• "}
  .diagnoses--a{left:36px}
  .diagnoses--b{left:204px}
  .diagnoses--c{left:324px;width:150px}
  .funding{position:absolute;left:36px;top:594px;width:430px;display:flex;justify-content:space-between}
  .funding-item{display:flex;align-items:center;gap:8px;font-size:7.6px;font-weight:500;line-height:1.3}
  .funding-num{font-family:"Jost",sans-serif;font-size:22px;font-weight:500}
  .hours{position:absolute;left:36px;top:630px;width:430px;background:var(--white);color:var(--grey-dark);font-size:9.6px;padding:3px 8px;display:flex;gap:8px;white-space:nowrap}
  .contact{position:absolute;left:36px;top:662px;width:430px;font-family:"Jost",sans-serif;font-weight:500;font-size:11px;letter-spacing:1.2px;line-height:1.4;font-style:normal}
  .contact-left{position:absolute;left:0;top:0}
  .contact-right{position:absolute;right:0;top:0;text-align:right}
  .contact-bottom{position:absolute;left:0;top:32px;width:430px;white-space:nowrap}

  /* front panel */
  .panel--front{background:var(--paper)}
  .cover-photo{position:absolute;left:0;top:0;width:500px;height:335px;background:
    radial-gradient(circle at 25% 60%,var(--photo-warm) 0%,rgba(224,164,78,0) 45%),
    radial-gradient(circle at 85% 55%,var(--photo-dark) 0%,rgba(93,80,71,0) 50%),
    linear-gradient(120deg,var(--photo-cool),#b9a892 60%,var(--photo-dark))}
  .brand{position:absolute;left:36px;top:34px;background:var(--white);padding:8px 14px;border-radius:8px;display:flex;align-items:center;gap:8px;font-family:"Jost",sans-serif;font-weight:500;font-size:15px;letter-spacing:1px;color:var(--sage-dark);text-transform:uppercase}
  .brand-dot{width:10px;height:10px;border-radius:50%;background:var(--sage-dark)}
  .quote-mark{position:absolute;left:34px;top:352px}
  .statement{position:absolute;left:36px;width:210px;color:var(--grey-dark)}
  .statement h3{font-family:"Jost",sans-serif;font-weight:500;font-size:13px;letter-spacing:1px;line-height:1.1;color:var(--sage-dark);text-transform:uppercase;margin-bottom:6px}
  .statement p{font-size:8.2px;font-style:italic;font-weight:500;line-height:1.4}
  .statement--mission{top:456px}
  .statement--vision{top:560px}
  .front-url{position:absolute;left:36px;top:688px;font-family:"Jost",sans-serif;font-size:11px;letter-spacing:1.6px;color:var(--grey)}
  .about-shadow{position:absolute;left:260px;top:328px;width:204px;height:362px;background:var(--shadow)}
  .about{position:absolute;left:268px;top:318px;width:204px;height:362px;background:var(--sage);color:var(--white);padding:22px 16px}
  .about h2{font-family:"Jost",sans-serif;font-weight:500;font-size:36px;line-height:1.15;letter-spacing:1.5px;text-transform:uppercase;margin-bottom:12px;white-space:nowrap}
  .about p{font-size:9px;line-height:1.36}
</style>
</head>
<body>
<main class="brochure">

  <section class="panel panel--back">
    <h1 class="headline">Why our approach<br>to brain injury is unique</h1>
    <div class="approach">
      <p>In more traditional therapy settings such as programs using outpatient models, attempts are made to simulate functional activities, combined with more structured tasks, all performed within their clinic environment. However, the inability to generalize learning has been shown to be a reoccurring difficulty for individuals with Traumatic Brain Injury and can often manifest in cognitive inflexibility, which makes carryover of their learned skills to the real world, a challenge.</p>
      <p>Community-based treatment circumvents this difficulty by conducting therapy in the person's home, school, workplace, or other settings within their community, such as a grocery store or at a post office. Clinicians are therefore able to witness first hand where a task is experiencing success or breaking down and can structure treatment accordingly. This allows for greater natural development of functional skills, with generalization issues no longer an obstacle toward meeting treatment goals.</p>
      <p>At Harborline Therapy Group we are committed to helping people recover their cognitive, physical and psycho-social abilities following brain injury through intensive individual treatment which focuses on safety, skill building and increasing independence, community reintegration, and overall life satisfaction. Our treatment approach is two-fold, with emphasis not only on direct restoration of brain functions, but also on helping the individual learn compensatory strategies (e.g., internal mnemonics, organizational systems, self-cuing techniques) or acquire assistive devices (e.g., planners, electronic reminders). Such methods are designed to reduce the effects of real-world disability when there is enduring cognitive impairment, and are most effective when introduced within a person's own relevant environments.</p>
    </div>

    <h2 class="serve-title">Who<br>we serve</h2>
    <div class="serve-intro">
      <p>We treat adults and adolescents with a variety of diagnoses. We service home and community locations throughout Southeast and mid-Michigan.</p>
      <p>Our therapists hold a variety of certifications and endorsements including CBIS (Certified Brain Injury Specialist), SwallowCare, and VoiceStrong.</p>
    </div>

    <div class="tag tag--diagnoses">Diagnoses can include:</div>
    <ul class="diagnoses diagnoses--a">
      <li>Traumatic Brain Injury</li>
      <li>Postconcussional Syndrome</li>
      <li>Spinal Cord Injury</li>
      <li>Post-traumatic Stress Disorder</li>
      <li>Depression</li>
    </ul>
    <ul class="diagnoses diagnoses--b">
      <li>Anxiety</li>
      <li>Mood Disorders</li>
      <li>Visual Impairments</li>
      <li>Balance Disorders</li>
      <li>Movement Disorders</li>
    </ul>
    <ul class="diagnoses diagnoses--c">
      <li>Neuromuscular Pathologies</li>
      <li>Dysphagia</li>
      <li>Musculoskeletal/Orthopedic injuries (ie. Spinal fractures/pathology, nerve injuries, pain)</li>
    </ul>

    <div class="tag tag--funding">Funding sources include:</div>
    <div class="funding">
      <div class="funding-item"><span class="funding-num">1</span><span>No-Fault<br>Auto Insurance</span></div>
      <div class="funding-item"><span class="funding-num">2</span><span>Workers Compensation<br>Insurance</span></div>
      <div class="funding-item"><span class="funding-num">3</span><span>Some Commercial Health<br>Insurance Carriers</span></div>
    </div>

    <div class="hours"><span>Office Hours: Monday – Friday 9:00 am – 4:30 pm</span><span>|</span><span>Therapy Hours: By Appointment</span></div>

    <address class="contact">
      <div class="contact-left">Fax: 555-014-2290<br>Phone: Office 555-014-2280</div>
      <div class="contact-right">1200 Maple Ridge Drive,<br>Suite 300 Fairview, ST 00000</div>
      <div class="contact-bottom">intake@harborline-therapy.com &nbsp;|&nbsp; www.harborline-therapy.com</div>
    </address>
  </section>

  <section class="panel panel--front">
    <div class="cover-photo" role="img" aria-label="Photo of three friends laughing together outdoors in warm sunlight"></div>
    <div class="brand"><span class="brand-dot"></span>Harborline Therapy Group</div>

    <svg class="quote-mark" width="90" height="72" viewBox="0 0 90 72" aria-hidden="true">
      <path d="M14 0 H38 L22 68 H0 Z" fill="var(--grey)"/>
      <path d="M62 0 H86 L70 68 H48 Z" fill="var(--grey)"/>
    </svg>

    <div class="statement statement--mission">
      <h3>Mission<br>statement</h3>
      <p>Our mission is to provide high quality therapy that allows the people we serve to achieve an optimal level of functioning and to improve their quality of life.</p>
    </div>
    <div class="statement statement--vision">
      <h3>Vision<br>statement</h3>
      <p>To be a recognized leader in functional rehabilitation to individuals with a variety of diagnoses in the home and community-based setting with an emphasis on goal-directed individual rehabilitation for addressing safety, skill building, independence, and cognitive and physical recovery.</p>
    </div>
    <div class="front-url">www.harborline-therapy.com</div>

    <div class="about-shadow"></div>
    <div class="about">
      <h2>Who<br>we are</h2>
      <p>For over 25 years, our company has been using evidence-based principles of rehabilitation to assist patients with their recovery. We are out in the real world with patients every day, helping them to get their lives back. Our goal is to provide functional home and community-based therapy to provide patient-centered holistic therapy with a state-of-the-art approach. Using the patient's natural environment such as their home, community or workplace allows us to attain measurable outcomes that turn even small successes into something bigger.</p>
    </div>
  </section>

</main>
</body>
</html>
```